Varnel Supply requires a new business card.

We are an online professional tool store.

Target Market(s)

We target the professional technician.

Industry/Entity Type

Business

Contact Information for Business Card

VarnelSupply.com.au

sales@varnelsupply.example

Requirements
Must have
• Needs to look commercial and professional
Should not have
• No Australian Colors, maps or shapes.
• No Shapes of Tools

```html
<!DOCTYPE html>
<html lang="en">
<head>
<meta charset="utf-8">
<title>Varnel Supply — Business Card</title>
<link rel="stylesheet" href="https://fonts.googleapis.com/css2?family=Roboto:wght@400;500;700&family=Roboto+Condensed:wght@700&display=swap">
<style>
  :root {
    --bg: #2a2a2b;
    --card: #f2f2f2;
    --brand-blue: #0b24a9;
    --accent-blue: #1f9bd6;
    --text-light: #ffffff;
    --text-grey: #4a4a4a;
  }
  * { margin: 0; padding: 0; box-sizing: border-box; }
  html, body { width: 1200px; height: 960px; overflow: hidden; }
  body {
    background: var(--bg);
    font-family: "Roboto", Arial, sans-serif;
    position: relative;
  }
  .card {
    position: absolute;
    width: 600px;
    height: 342px;
    border-radius: 18px;
    background: var(--card);
    overflow: hidden;
  }
  .card--front { left: 314px; top: 113px; }
  .card--back { left: 311px; top: 472px; }

  .front-panel { position: absolute; inset: 0; }

  .holder { position: absolute; left: 36px; top: 38px; }
  .holder__name {
    font-family: "Roboto Condensed", Arial, sans-serif;
    font-weight: 700;
    font-size: 20px;
    color: var(--accent-blue);
    line-height: 1;
  }
  .holder__role {
    margin-top: 7px;
    font-weight: 500;
    font-size: 14px;
    color: var(--text-light);
  }

  .address {
    position: absolute; left: 36px; top: 166px;
    font-size: 14px; line-height: 19px; color: var(--text-light);
  }
  .contacts {
    position: absolute; left: 36px; top: 212px;
    list-style: none; font-size: 14px; line-height: 19px; color: var(--text-light);
  }
  .contacts li { display: flex; align-items: center; gap: 8px; }
  .contacts svg { width: 14px; height: 14px; fill: var(--accent-blue); flex: none; }

  .wordmark {
    position: absolute;
    font-weight: 700;
    color: var(--brand-blue);
    white-space: nowrap;
  }
  .card--front .wordmark { left: 352px; top: 146px; font-size: 34px; }
  .card--back .wordmark { left: 0; right: 0; top: 134px; text-align: center; font-size: 40px; }

  .back-url {
    position: absolute; left: 0; right: 0; top: 288px;
    text-align: center; font-size: 15px; letter-spacing: 2.4px; color: var(--text-grey);
  }
</style>
</head>
<body>

<section class="card card--front" aria-label="Business card front">
  <svg class="front-panel" viewBox="0 0 600 342" aria-hidden="true">
    <path d="M0 0 H330 Q144 171 406 342 H0 Z" fill="var(--brand-blue)"/>
  </svg>

  <div class="holder">
    <p class="holder__name">NORA BELLAMY</p>
    <p class="holder__role">CEO/FOUNDER</p>
  </div>

  <p class="address">4120 Larkspur Road<br>Fairbanks, Alaska 31862</p>

  <ul class="contacts">
    <li><svg viewBox="0 0 16 16"><path d="M3 1l3 3-2 2c1 2 3 4 5 5l2-2 3 3-2 3C6 15 1 10 1 3z"/></svg>614 205 7731</li>
    <li><svg viewBox="0 0 16 16"><path d="M4 0h8v16H4zM5.5 2v10h5V2zM7 13h2v1.5H7z" fill-rule="evenodd"/></svg>852 319 4406</li>
    <li><svg viewBox="0 0 16 16"><path d="M4 1h8v4H4zM1 6h14v7h-3v2H4v-2H1zM5 11v3h6v-3z" fill-rule="evenodd"/></svg>473 560 2189</li>
    <li><svg viewBox="0 0 16 16"><path d="M1 3h14v10H1zM2 4l6 5 6-5z" fill-rule="evenodd"/></svg>sales@varnelsupply.example</li>
    <li><svg viewBox="0 0 16 16"><circle cx="8" cy="8" r="7"/><path d="M1 8h14M8 1c-3 3-3 11 0 14M8 1c3 3 3 11 0 14" stroke="#0b24a9" stroke-width="1" fill="none"/></svg>VarnelSupply.com.au</li>
  </ul>

  <p class="wordmark">Varnel Supply</p>
</section>

<section class="card card--back" aria-label="Business card back">
  <p class="wordmark">Varnel Supply</p>
  <p class="back-url">www.VarnelSupply.com.au</p>
</section>

</body>
</html>
```